BFCM Creatives Theme

We are looking for an initial design for our BFCM campaign this year to set the theme for all other creatives for BFCM. We are an ecommerce brand selling Merino wool baby clothing. Our flagship product is the Cozy Nestling Drift Cocoon (see images).

We are starting with the request for an instagram post, announcing the sale (details below). This post should be 1080x1350 but also look appealing in the square grid. I've attached a basic brand card showing color palette, fonts, and logos. I will also attach some image options. We are looking for your creativity to shine while aligning with our branding and connecting with the customer. If you have a specific idea and are looking for a specific image please contact us.

Sale Details:
- 20% Off Sitewide
- 11.28.24 - 12.02.24
- Excluding giftcards and imperfects. No rainchecks.

```html
<!DOCTYPE html>
<html lang="en">
<head>
<meta charset="utf-8">
<title>Lanalumi — 20% Off Sitewide</title>
<link href="https://fonts.googleapis.com/css2?family=Poppins:wght@600;700;800&family=Kalam:wght@300&display=swap" rel="stylesheet">
<style>
  :root {
    --charcoal: #333336;
    --off-white: #efeeec;
    --stone: #a9a596;
    --sand-top: #ccbca0;
    --sand-bottom: #b8a182;
    --page-bg: #6e6e6e;
    --white: #ffffff;
  }
  html, body {
    margin: 0;
    padding: 0;
    width: 1200px;
    height: 1197px;
    overflow: hidden;
    background: var(--page-bg);
  }
  .stage {
    position: relative;
    width: 1200px;
    height: 1197px;
  }
  .post {
    position: absolute;
    left: 146px;
    top: 31px;
    width: 1080px;
    height: 1350px;
    transform: scale(0.84);
    transform-origin: top left;
    overflow: hidden;
    font-family: "Poppins", sans-serif;
  }
  .product-photo {
    position: absolute;
    left: 444px; top: 0;
    width: 636px; height: 1350px;
    background: linear-gradient(180deg, var(--sand-top) 0%, #c6b597 40%, var(--sand-bottom) 100%);
  }
  .info-panel {
    position: absolute;
    left: 0; top: 0;
    width: 444px; height: 1255px;
    background: var(--charcoal);
  }
  .bar { position: absolute; background: var(--off-white); }
  .bar--tl-1 { left: 2px; top: 22px; width: 154px; height: 25px; }
  .bar--tl-2 { left: 2px; top: 73px; width: 154px; height: 27px; }
  .bar--br-1 { left: 927px; top: 1009px; width: 153px; height: 26px; }
  .bar--br-2 { left: 927px; top: 1061px; width: 153px; height: 26px; }
  .block { position: absolute; background: var(--stone); }
  .block--top { left: 741px; top: 0; width: 339px; height: 32px; }
  .block--square { left: 962px; top: 54px; width: 86px; height: 86px; }
  .block--bottom { left: 0; top: 1255px; width: 549px; height: 95px; }

  .headline {
    position: absolute;
    left: 40px; top: 160px;
    margin: 0;
    color: var(--white);
    font-weight: 800;
    line-height: 0.86;
    letter-spacing: -2px;
  }
  .headline__percent { display: block; font-size: 196px; }
  .headline__off { display: block; font-size: 182px; margin-left: 6px; }

  .scope-band {
    position: absolute;
    left: 0; top: 503px;
    width: 444px; height: 112px;
    background: var(--off-white);
  }
  .scope-band__text {
    position: absolute;
    left: 44px; top: 8px;
    margin: 0;
    font-size: 82px;
    font-weight: 700;
    color: var(--charcoal);
    letter-spacing: 0.5px;
  }
  .calendar-icon {
    position: absolute;
    left: 182px; top: 668px;
    width: 70px; height: 76px;
  }
  .sale-dates {
    position: absolute;
    left: 0; top: 752px;
    width: 452px;
    margin: 0;
    text-align: center;
    color: var(--white);
    font-size: 43px;
    font-weight: 700;
    letter-spacing: -0.5px;
  }
  .terms {
    position: absolute;
    left: 44px; top: 834px;
    width: 380px;
    margin: 0; padding: 0;
    list-style: none;
    font-family: "Kalam", cursive;
    font-weight: 300;
    font-size: 39px;
    line-height: 55px;
    color: var(--white);
  }
  .terms li {
    position: relative;
    padding-left: 44px;
    margin-bottom: 20px;
  }
  .terms li::before {
    content: "";
    position: absolute;
    left: 3px; top: 25px;
    width: 15px; height: 15px;
    border-radius: 50%;
    background: var(--white);
  }
  .brand-band {
    position: absolute;
    left: 2px; top: 1048px;
    width: 710px; height: 90px;
    background: var(--off-white);
    display: flex;
    align-items: center;
    justify-content: center;
    gap: 16px;
    padding-left: 140px;
    box-sizing: border-box;
  }
  .brand-band__mark {
    width: 52px; height: 52px;
    border-radius: 50%;
    background: var(--charcoal);
  }
  .brand-band__name {
    font-size: 54px;
    font-weight: 600;
    color: var(--charcoal);
    letter-spacing: -0.5px;
  }
</style>
</head>
<body>
<div class="stage">
  <article class="post">
    <div class="product-photo" role="img" aria-label="Stack of folded printed merino baby sleep sacks on a wooden stool against a warm beige wall"></div>

    <section class="info-panel">
      <h1 class="headline">
        <span class="headline__percent">20%</span>
        <span class="headline__off">OFF</span>
      </h1>
    </section>

    <div class="scope-band"><p class="scope-band__text">Sitewide</p></div>

    <svg class="calendar-icon" viewBox="0 0 70 76" aria-hidden="true">
      <rect x="3" y="10" width="64" height="62" rx="8" fill="none" stroke="#ffffff" stroke-width="5"/>
      <line x1="3" y1="24" x2="67" y2="24" stroke="#ffffff" stroke-width="5"/>
      <rect x="15" y="2" width="7" height="16" rx="3" fill="#ffffff"/>
      <rect x="48" y="2" width="7" height="16" rx="3" fill="#ffffff"/>
      <g fill="#ffffff">
        <rect x="12" y="32" width="9" height="8"/><rect x="25" y="32" width="9" height="8"/><rect x="38" y="32" width="9" height="8"/><rect x="51" y="32" width="8" height="8"/>
        <rect x="12" y="44" width="9" height="8"/><rect x="25" y="44" width="9" height="8"/><rect x="38" y="44" width="9" height="8"/><rect x="51" y="44" width="8" height="8"/>
        <rect x="12" y="56" width="9" height="8"/><rect x="25" y="56" width="9" height="8"/><rect x="38" y="56" width="9" height="8"/>
      </g>
    </svg>

    <p class="sale-dates">11.28.24 - 12.02.24</p>

    <ul class="terms">
      <li>Excluding giftcards and imperfects</li>
      <li>No rainchecks</li>
    </ul>

    <div class="bar bar--tl-1"></div>
    <div class="bar bar--tl-2"></div>
    <div class="block block--top"></div>
    <div class="block block--square"></div>
    <div class="bar bar--br-1"></div>
    <div class="bar bar--br-2"></div>
    <div class="block block--bottom"></div>

    <div class="brand-band">
      <span class="brand-band__mark"></span>
      <span class="brand-band__name">Lanalumi</span>
    </div>
  </article>
</div>
</body>
</html>
```